Your Vorrant App all-in-one system for transformation needs a book cover.

Hello- I would like a very similar book cover ( Beneath The Quiet Orchard book cover) as the sample I'm attaching. The person on my book cover would be less stiff, wear a cowboy hat, and maybe have flying hair. High-end bohemian style. Our brand colors are gold, light pink, and tan color. I'll attach App Logo and the colors we used on that. The title of my book is: "The Radiant Harbor Practice" and I will also need formatting for ebook, audio, and paperback. Thank you, Lorna

Target Market(s)

Those who are on the path to enlightenment - 60% women 40% men

Industry/Entity Type

Consciousness Industry

Font styles to use
Other font styles liked:
• Dubai

Colors
0054AA
0677BA
7BADD7
CADEEF
E8F1F8
FFC000
F8CF3A
FAE287
FDF2CF
FEFAEE
F0912C
F2A743
F7CA91
FBE8D2
FDF5EE
EE7325
F08F49
F5BC92
FAE3D3
FDF4ED
6B429C
8869AF
B7A5CE
E3DAEB
F3F0F8

Requirements
Must have
• Light spheres - light pink, orange-pink, gold and possibly blue on the very top
Should not have
• More of a sun rise feel, less or no clouds in the upper section,

```html
<!DOCTYPE html>
<html lang="en">
<head>
<meta charset="utf-8">
<title>The Radiant Harbor Practice — Book Cover</title>
<link href="https://fonts.googleapis.com/css2?family=Jost:wght@500;600;700&display=swap" rel="stylesheet">
<style>
  :root {
    --backdrop: #dcdedc;
    --sky-top: #6a4f7e;
    --sky-plum: #874465;
    --sky-rose: #c4586a;
    --sun-gold: #f8d88c;
    --sun-core: #fbe6a6;
    --horizon-amber: #e7932f;
    --ground-dark: #24141a;
    --type-light: #f3e4df;
    --type-author: #e6d2cc;
  }
  * { margin: 0; padding: 0; box-sizing: border-box; }
  html, body {
    width: 1200px;
    height: 1013px;
    overflow: hidden;
    background: var(--backdrop);
  }
  .book-cover {
    position: absolute;
    left: 346px;
    top: 154px;
    width: 507px;
    height: 716px;
    overflow: hidden;
    font-family: "Jost", "Futura", sans-serif;
  }
  .cover-art {
    position: absolute;
    inset: 0;
    width: 100%;
    height: 100%;
    display: block;
  }
  .title {
    position: absolute;
    left: 0;
    right: 0;
    top: 42px;
    text-align: center;
    color: var(--type-light);
    font-weight: 700;
    font-size: 64px;
    line-height: 101px;
    letter-spacing: 0.2em;
    text-transform: uppercase;
    text-shadow: 0 0 6px rgba(255, 236, 230, 0.45);
  }
  .title-line {
    display: block;
    margin-right: -0.2em;
    opacity: 0.93;
  }
  .author {
    position: absolute;
    left: 0;
    right: 0;
    top: 568px;
    text-align: center;
    color: var(--type-author);
    font-weight: 700;
    font-size: 46px;
    line-height: 46px;
    letter-spacing: 0.24em;
    text-transform: uppercase;
  }
  .author-line {
    display: block;
    margin-right: -0.24em;
  }
  .series-line {
    position: absolute;
    left: 0;
    right: 0;
    top: 677px;
    text-align: center;
    color: var(--type-light);
    font-weight: 600;
    font-size: 14px;
    letter-spacing: 0.08em;
    text-transform: uppercase;
  }
</style>
</head>
<body>
  <main class="book-cover">
    <svg class="cover-art" viewBox="0 0 507 716" preserveAspectRatio="none" role="img" aria-label="Illustration of a lone figure walking through tall grass toward a glowing sunrise under rose and violet skies">
      <defs>
        <linearGradient id="skyGradient" x1="0" y1="0" x2="0" y2="1">
          <stop offset="0" stop-color="var(--sky-top)"/>
          <stop offset="0.3" stop-color="var(--sky-plum)"/>
          <stop offset="0.55" stop-color="var(--sky-rose)"/>
          <stop offset="0.72" stop-color="var(--sun-gold)"/>
          <stop offset="0.82" stop-color="var(--horizon-amber)"/>
          <stop offset="0.9" stop-color="#5a2a24"/>
          <stop offset="1" stop-color="var(--ground-dark)"/>
        </linearGradient>
        <radialGradient id="sunGlow" cx="0.5" cy="0.62" r="0.45">
          <stop offset="0" stop-color="var(--sun-core)" stop-opacity="0.95"/>
          <stop offset="0.5" stop-color="var(--sun-gold)" stop-opacity="0.55"/>
          <stop offset="1" stop-color="var(--sun-gold)" stop-opacity="0"/>
        </radialGradient>
      </defs>
      <rect width="507" height="716" fill="url(#skyGradient)"/>
      <rect width="507" height="716" fill="url(#sunGlow)"/>
    </svg>

    <h1 class="title">
      <span class="title-line">The</span>
      <span class="title-line">Radiant</span>
      <span class="title-line">Harbor</span>
      <span class="title-line">Practice</span>
    </h1>

    <p class="author">
      <span class="author-line">Owen</span>
      <span class="author-line">Harte</span>
    </p>

    <p class="series-line">Elias Thornwood | Book Two</p>
  </main>
</body>
</html>
```